Brackenfold Latches Business Cards

Need high quality business card designed around my company logo. Ideally the cards need to be a glossy black as the logo goes well with a black background.

The company is a Locksmithing business.

Domestic clients are Residential Home Owners and Landlords. Commercial clients are local businesses, estate agents, landlords, solicitors

Services offered :
Emergency Lock Out
New Lock Fitting & Replacement
High Security Upgrades
UPVC lock repairs
Mobile Key Cutting
Free Security Reviews

Qualificatons & Certifications:
Accredited Guild & Tower KSR Level 3, QTRB
Fully Insured
PVX Checked

Contact & Business Details:

Business Name : Brackenfold Latches
Name: Rob Fenwick
Tel: 01823 574419 Office / 07841592637 Mobile
Email: contact@brackenfoldlatches.com
Website: www.brackenfoldlatches.com

(please note that the website is currently under development and not available to view)

Locksmith

Name: Rob Fenwick

Services:
Emergency Lock Out
High Security Upgrades
UPVC lock repairs
Mobile Key Cutting
Free Security Reviews

• Ideally the cards should be a glossy black as the logo stands out better on a black background.

Logo on front and the word LOCKSMITH should be incorporated into the front design of the card.

Qualifications & Certifications on the back ideally along the top / bottom of the card or split (I.e along the top “ Accredited : Guild & Tower Level 3 , QTRB”
and along the bottom , “Fully Insured & PVX Checked”

Services offered ideally listed on the back of the card, preferably split into two columns. If possible the logo could also be incorporated onto the back of the card between the two services columns (I.e the services listed either side of the logo)
• On the back of the card, have the logo in the middle with the services listed either side of the logo I.e 3 services on left of logo and three to the right.

```html
<!DOCTYPE html>
<html lang="en">
<head>
<meta charset="utf-8">
<title>Brackenfold Latches – Business Cards</title>
<link rel="stylesheet" href="https://fonts.googleapis.com/css2?family=Open+Sans:wght@400;600;700&display=swap">
<style>
  :root {
    --bg: #3a3a3b;
    --card: #141414;
    --card-edge: #b8912f;
    --gold-light: #f1d27a;
    --gold: #d9a93c;
    --gold-deep: #a9772a;
    --rule: #8a6a25;
  }
  * { box-sizing: border-box; margin: 0; padding: 0; }
  html, body { width: 1200px; height: 801px; overflow: hidden; }
  body {
    background: var(--bg);
    font-family: "Open Sans", Arial, sans-serif;
    display: flex;
    align-items: center;
    justify-content: center;
    gap: 40px;
  }
  .card {
    position: relative;
    width: 540px;
    height: 340px;
    background: var(--card);
    border: 2px solid var(--card-edge);
    border-radius: 18px;
    overflow: hidden;
  }
  .brand-mark {
    position: absolute;
    left: 28px;
    top: 0;
    width: 200px;
    height: 100%;
    display: flex;
    align-items: center;
    justify-content: center;
    text-align: center;
  }
  .brand-name {
    font-weight: 700;
    font-size: 30px;
    line-height: 1.15;
    color: var(--gold);
    text-transform: uppercase;
    letter-spacing: 1px;
  }
  .divider {
    position: absolute;
    left: 250px;
    top: 50px;
    width: 1px;
    height: 180px;
    background: linear-gradient(to bottom, transparent, var(--rule), transparent);
  }
  .card--front .divider { top: 70px; height: 200px; }

  .contact-block {
    position: absolute;
    left: 278px;
    top: 100px;
  }
  .person-name {
    font-weight: 700;
    font-size: 22px;
    color: var(--gold-light);
    letter-spacing: 0.5px;
    margin-bottom: 14px;
  }
  .person-name span { color: var(--gold); }
  .contact-list { list-style: none; }
  .contact-list li {
    display: flex;
    align-items: center;
    gap: 8px;
    font-size: 14px;
    color: var(--gold);
    line-height: 24px;
  }
  .contact-list svg { width: 12px; height: 12px; fill: var(--gold-light); flex: none; }

  .service-list {
    position: absolute;
    left: 278px;
    top: 46px;
    list-style: none;
  }
  .service-list li {
    font-weight: 600;
    font-size: 16px;
    line-height: 31px;
    color: var(--gold-deep);
  }
  .service-list li b { font-weight: 600; color: var(--gold-light); }

  .credentials {
    position: absolute;
    left: 0;
    right: 0;
    bottom: 26px;
    text-align: center;
    font-size: 15px;
    line-height: 22px;
    color: var(--gold);
  }
  .credentials .sep { margin: 0 10px; }
</style>
</head>
<body>

  <section class="card card--front" aria-label="Business card front">
    <div class="brand-mark">
      <span class="brand-name">Brackenfold<br>Latches</span>
    </div>
    <div class="divider"></div>
    <div class="contact-block">
      <h1 class="person-name">ROB <span>FENWICK</span></h1>
      <ul class="contact-list">
        <li>
          <svg viewBox="0 0 24 24" aria-hidden="true"><path d="M6.6 10.8a15.1 15.1 0 0 0 6.6 6.6l2.2-2.2a1 1 0 0 1 1-.25 11.4 11.4 0 0 0 3.6.57 1 1 0 0 1 1 1V20a1 1 0 0 1-1 1A17 17 0 0 1 3 4a1 1 0 0 1 1-1h3.5a1 1 0 0 1 1 1c0 1.25.2 2.45.57 3.57a1 1 0 0 1-.25 1z"/></svg>
          01823 574419
        </li>
        <li>
          <svg viewBox="0 0 24 24" aria-hidden="true"><path d="M7 1h10a2 2 0 0 1 2 2v18a2 2 0 0 1-2 2H7a2 2 0 0 1-2-2V3a2 2 0 0 1 2-2zm0 3v14h10V4z"/></svg>
          07841592637
        </li>
        <li>
          <svg viewBox="0 0 24 24" aria-hidden="true"><path d="M2 5h20v14H2zm2 2v.5l8 5 8-5V7l-8 5z"/></svg>
          contact@brackenfoldlatches.com
        </li>
        <li>
          <svg viewBox="0 0 24 24" aria-hidden="true"><path d="M12 2a10 10 0 1 0 0 20 10 10 0 0 0 0-20zm6.9 9h-3a15 15 0 0 0-1.3-5.6A8 8 0 0 1 18.9 11zM12 4c.9 1.2 1.8 3.6 1.9 7h-3.8c.1-3.4 1-5.8 1.9-7zM9.4 5.4A15 15 0 0 0 8.1 11h-3a8 8 0 0 1 4.3-5.6zM5.1 13h3a15 15 0 0 0 1.3 5.6A8 8 0 0 1 5.1 13zM12 20c-.9-1.2-1.8-3.6-1.9-7h3.8c-.1 3.4-1 5.8-1.9 7zm2.6-1.4a15 15 0 0 0 1.3-5.6h3a8 8 0 0 1-4.3 5.6z"/></svg>
          www.brackenfoldlatches.com
        </li>
      </ul>
    </div>
  </section>

  <section class="card card--back" aria-label="Business card back">
    <div class="brand-mark" style="height:250px;">
      <span class="brand-name">Brackenfold<br>Latches</span>
    </div>
    <div class="divider"></div>
    <ul class="service-list">
      <li><b>Emergency</b> Lock Out</li>
      <li><b>New Lock</b> Fitting &amp; Replacement</li>
      <li><b>High Security</b> Upgrades</li>
      <li><b>UPVC lock</b> repairs</li>
      <li><b>Mobile Key</b> Cutting</li>
      <li><b>Free</b> Security Reviews</li>
    </ul>
    <p class="credentials">
      Accredited Guild &amp; Tower KSR Level 3, QTRB<br>
      Fully Insured<span class="sep">•</span>PVX Checked
    </p>
  </section>

</body>
</html>
```